Bright Horizon Painting and Remodeling needs a business card

Business card should have company logo. I will upload two different logos and let me see which one is a better design for the business card.

Name of company: Bright Horizon Painting and Remodeling
Address: 4126 NW 71st st Suite 214
Miami, FL 33166

local phone: (305) 555-0142
toll free (855) 555-0197
fax (866) 555-0163

email: corinne@paintingbrighthorizon.example

not sure if i should include social media links or names on the business card.

company does interior and exterior painting, pressure washing, wall paper removal, drywall and stucco repair, staining,

We give free estimates.

I want a two sided business card.

Not sure if all this information is necessary for the business card. Designer can pick out whatever information they deem is important for a consumer to see on the business card.

Anticipating on the business card to be printed on nice quality.

I will upload an image of one of the logos on a type of business card surface. That idea can be used as well. Be creative. Business card should be professional but very nice and eye catching.

remove drywall and stucco repair and replace with tile installation

Industry/Entity Type

Business

Contact Information for Business Card

Miami, FL 33166

toll free (855) 555-0197
fax (866) 555-0163

company does interior and exterior painting, pressure washing, wall paper removal, drywall and stucco repair, staining, tile removal, *specializing in vinyl floor removal

free estimates.

Requirements
Must have
• Profesional font

```html
<!DOCTYPE html>
<html lang="en">
<head>
<meta charset="utf-8">
<title>Bright Horizon Painting and Remodeling – Business Card</title>
<link rel="stylesheet" href="https://fonts.googleapis.com/css2?family=Source+Sans+3:wght@400;600&display=swap">
<style>
  :root {
    --backdrop: #2a2a2a;
    --card: #f4f4f4;
    --ink: #3a3a3a;
    --ink-soft: #444444;
    --accent-blue: #2e86c1;
    --icon-red: #d0393f;
    --white: #ffffff;
    --tone-warm: #f2b441;
    --tone-red: #de4a4a;
    --tone-cool: #4a7cc4;
  }
  * { box-sizing: border-box; margin: 0; padding: 0; }
  html, body {
    width: 1200px; height: 443px; overflow: hidden;
    background: var(--backdrop);
    font-family: "Source Sans 3", "Myriad Pro", sans-serif;
  }
  .canvas { position: relative; width: 1200px; height: 443px; }
  .card {
    position: absolute; top: 90px;
    width: 480px; height: 274px;
    background: var(--card);
    border-radius: 16px;
    overflow: hidden;
  }
  .card--front { left: 108px; }
  .card--back { left: 603px; }

  /* placeholder area for the watercolour splash artwork */
  .art-area {
    position: absolute;
    border-radius: 50%;
    background: linear-gradient(160deg, var(--tone-warm) 0%, var(--tone-red) 50%, var(--tone-cool) 100%);
    opacity: .55;
  }
  .art-area--logo { left: 40px; top: 30px; width 216px; width: 216px; height: 216px; }
  .art-area--front-edge { left: 326px; top: -10px; width: 300px; height: 300px; }
  .art-area--back-edge { left: -140px; top: -10px; width: 316px; height: 300px; }

  .disc {
    position: absolute; border-radius: 50%;
    background: var(--white);
    box-shadow: 0 0 6px rgba(0,0,0,.12);
  }
  .disc--logo {
    left: 98px; top: 90px; width: 98px; height: 98px;
    display: flex; align-items: center; justify-content: center; text-align: center;
  }
  .disc--front-edge { left: 414px; top: 68px; width: 172px; height: 172px; }
  .disc--back-edge { left: -85px; top: 66px; width: 176px; height: 176px; }

  .brand-name {
    font-size: 10px; font-weight: 600; line-height: 1.2;
    color: var(--ink); text-transform: uppercase; letter-spacing: .3px;
    width: 80px;
  }

  .details { position: absolute; left: 207px; top: 58px; color: var(--ink-soft); }
  .person-name { font-size: 18px; font-weight: 400; color: var(--ink); line-height: 1.1; }
  .job-title { font-size: 12px; color: var(--accent-blue); margin-top: 2px; }
  .contact-list { list-style: none; margin-top: 18px; font-size: 12px; line-height: 15px; }
  .contact-list li { display: flex; align-items: flex-start; margin-bottom: 6px; }
  .contact-list li.address { margin-bottom: 9px; }
  .contact-icon { width: 12px; height: 12px; margin: 2px 9px 0 0; flex: none; fill: var(--icon-red); }
</style>
</head>
<body>
<main class="canvas">
  <section class="card card--front" aria-label="Card front">
    <div class="art-area art-area--logo" role="img" aria-label="Rainbow watercolour paint splash around the company name"></div>
    <div class="disc disc--logo">
      <span class="brand-name">Bright Horizon Painting &amp; Remodeling</span>
    </div>
    <div class="art-area art-area--front-edge" role="img" aria-label="Rainbow watercolour paint splash"></div>
    <div class="disc disc--front-edge"></div>
  </section>

  <section class="card card--back" aria-label="Card back">
    <div class="art-area art-area--back-edge" role="img" aria-label="Rainbow watercolour paint splash"></div>
    <div class="disc disc--back-edge"></div>

    <div class="details">
      <p class="person-name">Your Name</p>
      <p class="job-title">Job Title</p>
      <ul class="contact-list">
        <li class="address">
          <svg class="contact-icon" viewBox="0 0 12 12" aria-hidden="true"><path d="M6 0a4 4 0 0 0-4 4c0 3 4 8 4 8s4-5 4-8a4 4 0 0 0-4-4zm0 5.6A1.6 1.6 0 1 1 6 2.4a1.6 1.6 0 0 1 0 3.2z"/></svg>
          <span>4126 NW 71st st Suite 214<br>Miami, FL 33166</span>
        </li>
        <li>
          <svg class="contact-icon" viewBox="0 0 12 12" aria-hidden="true"><path d="M1 4c0-1.5 2.2-2.5 5-2.5S11 2.5 11 4v1H8.5V4h-5v1H1z"/><rect x="2" y="5.5" width="8" height="5" rx="1"/></svg>
          <span>(305) 555-0142&nbsp; I &nbsp;(855) 555-0197(toll free)</span>
        </li>
        <li>
          <svg class="contact-icon" viewBox="0 0 12 12" aria-hidden="true"><rect x="3" y="1" width="6" height="4"/><rect x="1" y="5" width="10" height="6" rx="1"/></svg>
          <span>(866) 555-0163</span>
        </li>
        <li>
          <svg class="contact-icon" viewBox="0 0 12 12" aria-hidden="true"><path d="M1 3h10v6.5H1z"/><path d="M1 3l5 3.6L11 3" fill="none" stroke="#f4f4f4" stroke-width="1"/></svg>
          <span>corinne@paintingbrighthorizon.example</span>
        </li>
      </ul>
    </div>
  </section>
</main>
</body>
</html>
```